KTB - Redesign (PSD Files Only)

Requirements for the site:

1. We need our logo recreated, please use the same design and change colors to work on a white background

2. The site is a "Wizard" based site, that takes the customer through the process of creating a unique web presence that suits there needs

3.Colors Needed - Main "Dark Blue" Secondary = "Dark Grey" -Other = "Light Grey and White"

4.We need a CRISP CLEAN DESIGN, simple design

5.Wireframes are a general layout and may be modified by you to enhance the design

6. We want a complete web 5.0 look with big buttons and text boxes

7.The more personality the better

8. Current Site brightlarkworks.example

9.See attachments for wireframes

10. Designer should deliver PSD files, no coding is required

11. The portfolio wireframe, should look like the design of the pixelharbor portfolio template
Updates

KEEP IT SIMPLE.,.....

We like the moonquill scaffold style of designs

```html
<!DOCTYPE html>
<html lang="en">
<head>
<meta charset="utf-8">
<title>KTB – Custom Website Design</title>
<link rel="stylesheet" href="https://fonts.googleapis.com/css2?family=Ubuntu:wght@300;400;500;700&display=swap">
<style>
:root{
  --blue:#2450a8;
  --blue-dark:#1d3f8f;
  --blue-light:#3d6fcf;
  --grey-bg:#ececec;
  --grey-text:#7a7a7a;
  --text:#555;
  --dark:#2b2b2b;
  --dark-band:#333;
  --white:#fff;
}
*{box-sizing:border-box;margin:0;padding:0}
html,body{width:1123px;height:1200px;overflow:hidden;background:var(--white)}
body{font-family:"Ubuntu",sans-serif;color:var(--text);position:relative}
.abs{position:absolute}

/* header */
.site-header{position:absolute;left:0;top:0;width:1123px;height:56px;background:linear-gradient(#3a6cc8,#1f4aa2);border-bottom:1px solid #173b85}
.main-nav a{position:absolute;top:0;height:56px;line-height:58px;color:var(--white);font-size:14px;font-weight:300;text-decoration:none}
.nav-sep{position:absolute;top:0;width:1px;height:56px;background:#173b85;box-shadow:1px 0 0 #4d7ad0}
.social{position:absolute;top:16px;width:28px;height:28px;border-radius:50%;background:var(--white)}
.phone{position:absolute;left:880px;top:18px;color:var(--white);font-size:18px;font-weight:500}

/* hero */
.hero{position:absolute;left:0;top:56px;width:1123px;height:514px;background:radial-gradient(ellipse at 50% 40%,#f7f7f7,var(--grey-bg) 70%)}
.hero h1{position:absolute;left:0;top:20px;width:1123px;text-align:center;color:var(--blue);font-size:31px;font-weight:500}
.hero .lead{position:absolute;left:120px;top:60px;width:883px;text-align:center;color:var(--grey-text);font-size:13px;font-weight:300;line-height:25px}
.feature{position:absolute;width:160px;height:160px;border-radius:50%;background:var(--white);box-shadow:0 8px 10px -6px rgba(0,0,0,.18)}
.feature .art{position:absolute;left:35px;top:12px;width:90px;height:80px;border-radius:8px}
.feature .caption{position:absolute;left:0;width:160px;text-align:center;font-size:13px;font-weight:300;color:#666;line-height:17px}
.brand-mark{position:absolute;left:503px;top:118px;width:117px;text-align:center}
.brand-mark .name{color:var(--blue);font-size:30px;font-weight:700;letter-spacing:1px}
.brand-mark .sub{color:#999;font-size:9px;font-weight:300;margin-top:-2px}
.product-box{position:absolute;left:503px;top:172px;width:117px;height:164px;background:linear-gradient(135deg,#2d2d2d,#0f0f0f);border-right:6px solid #3a8f1c}
.quote{position:absolute;left:160px;top:340px;width:310px;text-align:center;color:#444;font-weight:300}
.quote .l1{font-size:28px}
.quote .l2{font-size:28px;margin-top:4px}
.quote .l2 b{color:var(--blue);font-weight:700}
.step{position:absolute;top:365px;width:41px;height:19px;background:#e1e1e1}
.step.active{background:#8a8a8a}
.step.active::after{content:"";position:absolute;left:15px;top:19px;border:5px solid transparent;border-top-color:#8a8a8a}
.step-label{position:absolute;left:499px;top:396px;color:var(--blue);font-size:13px;font-weight:300}
.project-input{position:absolute;left:271px;top:433px;width:402px;height:42px;background:var(--white);border:1px solid #dcdcdc;box-shadow:inset 0 1px 3px rgba(0,0,0,.08)}
.cta{position:absolute;left:684px;top:433px;width:167px;height:41px;background:linear-gradient(#2f62c0,#1e469d);border:1px solid #173b85;color:var(--white);font-size:13.5px;font-weight:700;text-align:center;line-height:41px;letter-spacing:.2px}

/* services */
.services .col{position:absolute;top:592px;width:225px}
.col h2{color:var(--blue);font-size:14px;font-weight:700;height:34px}
.col p{font-size:11.5px;font-weight:300;line-height:22.5px;color:#555;height:64px;width:212px}
.col ul{list-style:none}
.col li{font-size:11.5px;font-weight:300;line-height:22.5px;color:#555;padding-left:17px;position:relative;white-space:nowrap}
.col li::before{content:"";position:absolute;left:1px;top:9px;width:5px;height:5px;border-right:1.5px solid #333;border-bottom:1.5px solid #333;transform:rotate(-45deg)}

/* portfolio */
.portfolio{position:absolute;left:0;top:869px;width:1123px;height:249px;background:var(--dark)}
.portfolio .band{position:absolute;left:0;top:134px;width:1123px;height:115px;background:var(--dark-band)}
.thumb{position:absolute;top:45px;width:277px;height:162px}
.arrow{position:absolute;top:116px}

/* footer */
.copyright{position:absolute;left:121px;top:1158px;font-size:13.5px;font-weight:300;color:#444}
.partner-badge{position:absolute;left:779px;top:1135px;width:127px;height:45px;background:#f4f4f4;border:1px solid #d6d6d6;box-shadow:0 1px 2px rgba(0,0,0,.15)}
.consult{position:absolute;left:923px;top:1141px;text-align:center}
.consult .r{color:var(--blue);font-size:17px;font-weight:700}
.consult .c{color:#555;font-size:10px;font-weight:400;margin-top:1px}
</style>
</head>
<body>

<header class="site-header">
  <nav class="main-nav">
    <a href="#" style="left:121px">Home</a>
    <span class="nav-sep" style="left:171px"></span>
    <a href="#" style="left:187px">About Us</a>
    <span class="nav-sep" style="left:256px"></span>
    <a href="#" style="left:270px">Portfolio</a>
    <span class="nav-sep" style="left:335px"></span>
    <a href="#" style="left:349px">Contact Us</a>
    <span class="nav-sep" style="left:429px"></span>
  </nav>
  <span class="social" style="left:460px" aria-label="Social profile"></span>
  <span class="social" style="left:492px" aria-label="Social profile"></span>
  <span class="social" style="left:525px" aria-label="Social profile"></span>
  <span class="social" style="left:557px" aria-label="Social profile"></span>
  <span class="social" style="left:589px" aria-label="Social feed"></span>
  <span class="nav-sep" style="left:851px"></span>
  <svg class="abs" style="left:858px;top:17px" width="18" height="26" viewBox="0 0 18 26" aria-hidden="true">
    <path d="M4 2 L8 2 L9 8 L6 10 C7 14 9 17 12 19 L14 16 L17 19 L16 24 C8 24 2 14 2 6 Z" fill="#fff"/>
  </svg>
  <div class="phone">1-800-555-0142</div>
</header>

<section class="hero">
  <h1>Get a Custom Website Design in 21 Days or LESS!</h1>
  <p class="lead">Find out why we're the #1 custom website design marketplace.Our network of designers will create 50+ web design samples for you to choose and our marketing experts will pave the way for your success.</p>

  <div class="feature" style="left:123px;top:142px">
    <div class="art" role="img" aria-label="Photo of a support agent wearing a headset" style="background:linear-gradient(#d9c3b0,#f1ece7)"></div>
    <div class="caption" style="top:102px">24/7 Customer<br>Support</div>
  </div>

  <div class="brand-mark">
    <div class="name">KTB</div>
    <div class="sub">Kestrel Tide Builders</div>
  </div>
  <div class="product-box" role="img" aria-label="Product box illustration for the design package"></div>

  <div class="feature" style="left:685px;top:219px">
    <div class="art" role="img" aria-label="Collage of sample website designs" style="left:25px;top:22px;width:110px;height:66px;background:linear-gradient(#c9d3e3,#eef1f5)"></div>
    <div class="caption" style="top:100px">Save 1000's<br>On webdesign</div>
  </div>

  <div class="feature" style="left:842px;top:98px">
    <div class="art" role="img" aria-label="Gold money back guarantee seal" style="left:42px;top:8px;width:76px;height:76px;border-radius:50%;background:radial-gradient(#f3d36a,#c8921d)"></div>
    <div class="caption" style="top:88px">100%<br>Money Back<br>Guarantee</div>
  </div>

  <div class="quote">
    <div class="l1">100%&nbsp; No Obligation</div>
    <div class="l2"><b>FREE</b> Web Quote</div>
  </div>

  <span class="step active" style="left:496px"></span>
  <span class="step" style="left:542px"></span>
  <span class="step" style="left:587px"></span>
  <div class="step-label">STEP1</div>

  <div class="project-input" aria-label="Project name"></div>
  <div class="cta">START YOUR PROJECT</div>
</section>

<section class="services">
  <div class="col" style="left:121px">
    <h2>Why Choose KTB?</h2>
    <p>We are a full service design &amp; marketing companythat will handle everything</p>
    <ul>
      <li>Dedicated Project Manager</li>
      <li>SIngle Point Of Contact</li>
      <li>Marketing Coaches</li>
      <li>Low Cost</li>
      <li>50+ Design Samples foryou to choose</li>
    </ul>
  </div>
  <div class="col" style="left:346px">
    <h2>Web Services</h2>
    <p>We specialize in the following design services</p>
    <ul>
      <li>Web Design</li>
      <li>Ecommerce Design</li>
      <li>Web Programming</li>
      <li>Logo Design</li>
      <li>Stationary/Print Design</li>
      <li>Ad Design</li>
      <li>Email Template design.</li>
    </ul>
  </div>
  <div class="col" style="left:568px">
    <h2>Marketing Services</h2>
    <p>We handle all onlinemarketing including the following</p>
    <ul>
      <li>Paid Search Ads</li>
      <li>Local Listing Marketing</li>
      <li>Search EngineOptimization</li>
      <li>Email Marketing</li>
      <li>Social MediaMarketing.</li>
    </ul>
  </div>
  <div class="col" style="left:795px;top:595px">
    <h2>Maintainence Services</h2>
    <p>Let us maintain your site and save up to 50% on the following</p>
    <ul>
      <li>Website Hosting</li>
      <li>Software Upgrades</li>
      <li>Custom WebProgramming</li>
      <li>Website Marketing</li>
    </ul>
  </div>
</section>

<section class="portfolio">
  <div class="band"></div>
  <svg class="arrow" style="left:88px" width="24" height="38" viewBox="0 0 24 38" aria-label="Previous">
    <path d="M20 3 L5 19 L20 35" fill="none" stroke="#8a8a8a" stroke-width="5"/>
  </svg>
  <div class="thumb" style="left:123px;background:linear-gradient(#2e7d32 0 8%,#eef2f6 8% 30%,#c9a37a 30% 70%,#e6e9ee 70%)" role="img" aria-label="Portfolio sample: care services website"></div>
  <div class="thumb" style="left:424px;background:linear-gradient(#ffffff 0 20%,#4d7b63 20% 60%,#d9cbb2 60%)" role="img" aria-label="Portfolio sample: boutique shop website"></div>
  <div class="thumb" style="left:725px;background:linear-gradient(#1d1d1d 0 25%,#6b5a12 25% 30%,#2a2418 30% 100%)" role="img" aria-label="Portfolio sample: restaurant website"></div>
  <svg class="arrow" style="left:1012px" width="24" height="38" viewBox="0 0 24 38" aria-label="Next">
    <path d="M4 3 L19 19 L4 35" fill="none" stroke="#8a8a8a" stroke-width="5"/>
  </svg>
</section>

<footer>
  <div class="copyright">©2013 Company Kestrel Tide Builders , All Rights Reserved</div>
  <div class="partner-badge" role="img" aria-label="Partner badge"></div>
  <div class="consult">
    <div class="r">REQUEST</div>
    <div class="c">CONSULTATION</div>
  </div>
</footer>

</body>
</html>
```